High Design Value Gift Webstore Needs a Logo Design & Business Card Design

Design wanted: Logo and Business Card Design for an online store selling designer gifts (substantially Scandinavian design products). Business Card to feature Logo and company details on the front and the back to include discount/promotional code.

Site name: Harbor Lantern and Kin

Site purpose: Enable time poor people to quickly select high design value gifts for special occasions (weddings, anniversaries, housewarmings, corporate gifts etc)

Products: A small selection of carefully selected high design value products ranging in price and across three categories: Display, Functional, Fun

Site design: We will be using a modern minimal Quillmart theme and will also have a mobile site and an app. Our website is primarily black/white/grayscale - similar to this style: http://themes.quillmart.example/themes/minimal/styles/fashion

Target Market(s)

Customers with limited time who can quickly choose a gift from our pre selected range of 24 products.

Industry/Entity Type

Store

Logo Text

Harbor Lantern And Kin

Requirements
Must have
• Modern design with company name included in the design, design needs to be modern and work well with our website - sample website (http://themes.quillmart.example/themes/minimal/styles/fashion).

```html
<!DOCTYPE html>
<html lang="en">
<head>
<meta charset="utf-8">
<title>Harbor Lantern and Kin — Business Card</title>
<link rel="stylesheet" href="https://fonts.googleapis.com/css2?family=Questrial&display=swap">
<style>
  :root {
    --backdrop: #e9e7e6;
    --card: #ffffff;
    --ink: #111111;
    --mark-grey: #8a8a8a;
    --card-shadow: rgba(0, 0, 0, 0.18);
  }
  * { margin: 0; padding: 0; box-sizing: border-box; }
  html, body {
    width: 1200px;
    height: 800px;
    overflow: hidden;
    background: var(--backdrop);
  }
  .canvas {
    width: 1200px;
    height: 800px;
    display: flex;
    align-items: center;
    justify-content: center;
  }
  .business-card {
    width: 840px;
    height: 480px;
    background: var(--card);
    box-shadow: 0 10px 30px var(--card-shadow);
    display: flex;
    flex-direction: column;
    align-items: center;
    justify-content: center;
    font-family: "Questrial", "Century Gothic", sans-serif;
    color: var(--ink);
  }
  .brand {
    display: flex;
    flex-direction: column;
    align-items: center;
    margin-bottom: 34px;
  }
  .brand-square {
    width: 128px;
    height: 112px;
    background: var(--mark-grey);
    margin-bottom: 26px;
  }
  .brand-name {
    font-size: 46px;
    font-weight: 400;
    letter-spacing: 0.5px;
    line-height: 1;
  }
  .contact {
    font-style: normal;
    text-align: center;
    line-height: 1.5;
  }
  .contact-phone {
    font-size: 26px;
    letter-spacing: 1px;
  }
  .contact-web {
    font-size: 26px;
    letter-spacing: 0.3px;
  }
</style>
</head>
<body>
  <main class="canvas">
    <section class="business-card">
      <div class="brand">
        <span class="brand-square" aria-hidden="true"></span>
        <h1 class="brand-name">Harbor Lantern and Kin</h1>
      </div>
      <address class="contact">
        <p class="contact-phone">07700900418</p>
        <p class="contact-web">www.harborlanternandkin.example</p>
      </address>
    </section>
  </main>
</body>
</html>
```